Nalvo Crest Business card Design

we need a business card design that is modern , easy to read , and remember able. the business sells all aspects of cooking and cooling equipment for restaurants, bars, cafe and large domestic kitchens
our website : www.nalvocrestgroup.com

```html
<!DOCTYPE html>
<html lang="en">
<head>
<meta charset="UTF-8">
<title>Nalvo Crest Business Card</title>
<link rel="stylesheet" href="https://fonts.googleapis.com/css2?family=Lato:wght@400;700;900&display=swap">
<style>
  :root {
    --backdrop: #2a2a2a;
    --card: #ffffff;
    --brand-red: #e8202a;
    --brand-blue: #1aa0e0;
  }
  html, body {
    margin: 0;
    padding: 0;
    width: 1200px;
    height: 1000px;
    overflow: hidden;
    background: var(--backdrop);
    font-family: "Lato", sans-serif;
  }
  .business-card {
    position: absolute;
    left: 100px;
    top: 210px;
    width: 1000px;
    height: 580px;
    background: var(--card);
    box-shadow: 0 18px 40px rgba(0,0,0,0.55);
  }
  .accent {
    position: absolute;
  }
  .accent-top { top: 0; right: 0; width: 470px; height: 9px; background: var(--brand-red); }
  .accent-right { top: 0; right: 0; width: 9px; height: 200px; background: var(--brand-red); }
  .accent-left { bottom: 0; left: 0; width: 9px; height: 260px; background: var(--brand-blue); }
  .accent-bottom { bottom: 0; left: 0; width: 470px; height: 9px; background: var(--brand-blue); }

  .card-info {
    position: absolute;
    left: 70px;
    top: 80px;
    color: var(--brand-blue);
    font-size: 21px;
    line-height: 1.2;
  }
  .company-name {
    margin: 0 0 34px;
    color: var(--brand-red);
    font-weight: 900;
    font-size: 29px;
    line-height: 1.1;
    text-transform: uppercase;
  }
  .hours-title {
    margin: 0;
    color: var(--brand-red);
    font-weight: 700;
    font-size: 22px;
  }
  .hours { margin: 0 0 40px; }
  .address { margin: 0 0 44px; font-style: normal; }
  .contact-list { list-style: none; margin: 0; padding: 0; }
  .contact-list li { margin: 0; }
  .contact-label { color: var(--brand-red); font-weight: 700; }

  .brand-mark {
    position: absolute;
    left: 660px;
    top: 300px;
    display: flex;
    align-items: center;
    gap: 14px;
  }
  .brand-square {
    width: 26px;
    height: 26px;
    background: var(--brand-blue);
  }
  .brand-name {
    color: var(--brand-red);
    font-weight: 900;
    font-size: 38px;
    text-transform: uppercase;
    letter-spacing: 1px;
  }
</style>
</head>
<body>
  <div class="business-card">
    <span class="accent accent-top"></span>
    <span class="accent accent-right"></span>
    <span class="accent accent-left"></span>
    <span class="accent accent-bottom"></span>

    <div class="card-info">
      <h1 class="company-name">Orven Engineering Co. Ltd<br>Nalvo Crest</h1>
      <p class="hours-title">Office Hours :</p>
      <p class="hours">Mon-Sat: 8.00 A.M.- 6.00 P.M.</p>
      <address class="address">
        418 Nalvo Crest Bldg., Meridan Rd.,<br>
        Sathorn Vale, Linwick , Bangkok,<br>
        Thailand 10300
      </address>
      <ul class="contact-list">
        <li><span class="contact-label">P:</span> (66)-2-555-0142 , (66)-2-555-0147</li>
        <li><span class="contact-label">F:</span> (66)-2-555-0193</li>
        <li><span class="contact-label">E:</span> info@nalvocrestgroup.com</li>
        <li><span class="contact-label">W:</span> www.nalvocrestgroup.com</li>
      </ul>
    </div>

    <div class="brand-mark">
      <span class="brand-square"></span>
      <span class="brand-name">Nalvo Crest</span>
    </div>
  </div>
</body>
</html>
```